upgrade joomla to HTML5 on existing website

This project will need designer to improve/upgrade existing website that was designed from joomla (CMS) to HTML5. The current website code would not given and designer only can visit the site to take all info to migrate it to new design.
Some addition of new image, info and web action will be added here. The designer must provide all source code and step to modify the newly design web for future modification. The existing web site is www.meadowfoxtrail.com.
Requirements
Must have
- knowledge on:-
- HTML5
- Twitter dock configuration
- web mail configuration
- CMS

```html
<!DOCTYPE html>
<html lang="en">
<head>
<meta charset="utf-8">
<title>MeadowFoxTrail</title>
<link href="https://fonts.googleapis.com/css2?family=Source+Sans+3:wght@300;400;600;700&display=swap" rel="stylesheet">
<style>
:root{
  --red:#e8111f;
  --red-dark:#a5212d;
  --ink:#333;
  --muted:#8a8a8a;
  --panel:#ebebeb;
  --dark-btn:#3a3a3a;
  --nav-home:#f57c12;
  --nav-about:#ffcc00;
  --nav-products:#a6d40a;
  --nav-news:#14c7c7;
  --nav-contact:#676a9a;
  --nav-mail:#f7323a;
}
*{box-sizing:border-box;margin:0;padding:0}
html,body{width:1160px;height:1200px;overflow:hidden}
body{font-family:"Source Sans 3",sans-serif;color:var(--ink);background:#fff;position:relative}
.topbar{position:absolute;left:0;top:0;width:1160px;height:44px;background:#f8f8f8;border-bottom:1px solid #e2e2e2}
.contact-line{position:absolute;left:116px;top:14px;font-size:12px;color:var(--muted);display:flex;gap:14px;align-items:center}
.contact-line span{display:flex;align-items:center;gap:5px}
.social-top{position:absolute;left:838px;top:10px;display:flex;gap:4px}
.social-top i{width:23px;height:23px;border:1px solid #ddd;background:#fff;border-radius:2px;display:flex;align-items:center;justify-content:center}
.social-top i::after{content:"";width:9px;height:9px;border-radius:50%;background:#b5b5b5}
.brand{position:absolute;left:122px;top:72px;display:flex;align-items:center;gap:12px}
.brand-mark{width:66px;height:66px;border-radius:50%;background:var(--red)}
.brand-name{font-size:22px;font-weight:700;color:var(--red)}
.brand-tag{font-size:8px;font-weight:700;color:#555;letter-spacing:.3px;margin-bottom:3px}
.main-nav{position:absolute;left:447px;top:60px;display:flex}
.main-nav a{width:101px;height:100px;color:#fff;text-decoration:none;font-size:13px;text-align:center;display:flex;flex-direction:column;align-items:center;padding-top:14px;line-height:16px;position:relative}
.main-nav svg{width:34px;height:34px;margin-bottom:14px;flex:none}
.nav-home{background:var(--nav-home)}
.nav-home::after{content:"";position:absolute;bottom:0;left:44px;border:6px solid transparent;border-bottom-color:#fff}
.nav-about{background:var(--nav-about)}
.nav-products{background:var(--nav-products)}
.nav-news{background:var(--nav-news)}
.nav-contact{background:var(--nav-contact)}
.nav-mail{background:var(--nav-mail)}
.hero{position:absolute;left:0;top:186px;width:1160px;height:300px;background:linear-gradient(#ec1520,var(--red-dark))}
.hero-text{position:absolute;left:150px;top:64px;width:500px;text-align:center;color:#fff}
.hero-text h1{font-size:30px;font-weight:700;line-height:36px}
.hero-text p{font-size:23px;font-weight:400;line-height:29px}
.hero-visual{position:absolute;left:688px;top:14px;width:262px;height:262px;border-radius:50%;background:radial-gradient(circle at 40% 35%,#6fb2f0,#1d5fc7 60%,#173f8f)}
.slide-btn{position:absolute;width:50px;height:50px;background:var(--dark-btn);display:flex;align-items:center;justify-content:center}
.features{position:absolute;left:0;top:486px;width:1160px;height:358px;background:var(--panel)}
.features::before{content:"";position:absolute;left:100px;top:0;width:960px;height:14px;background:radial-gradient(ellipse at top,rgba(0,0,0,.18),transparent 70%)}
.card{position:absolute;top:40px;width:311px}
.card h2,.product-samples h2{font-size:23px;font-weight:400;color:#333}
.pager{position:absolute;display:flex;gap:2px}
.pager i{width:20px;height:20px;background:var(--dark-btn);display:flex;align-items:center;justify-content:center}
.card .photo{position:absolute;left:12px;top:42px;width:279px;height:102px}
.card p{position:absolute;left:12px;top:154px;width:284px;font-size:11.5px;line-height:24px;text-align:justify;color:#333}
.card .rule{position:absolute;left:0;top:250px;width:311px;height:4px;background:var(--red)}
.product-samples{position:absolute;left:0;top:844px;width:1160px;height:276px;border-top:3px solid #d8d8d8;background:#fff}
.product-samples .photo{position:absolute;top:54px;width:279px;height:186px}
.zoom{position:absolute;left:115px;top:61px;width:50px;height:44px;background:#f0163d;border-radius:7px;display:flex;align-items:center;justify-content:center}
.footer{position:absolute;left:0;top:1120px;width:1160px;height:80px;background:linear-gradient(#ed1822,var(--red-dark));color:#fff}
.footer nav{position:absolute;left:102px;top:18px;font-size:12px;display:flex;gap:10px}
.footer small{position:absolute;left:99px;top:38px;font-size:12px}
.social-foot{position:absolute;left:905px;top:18px;display:flex;gap:3px}
.social-foot i{width:35px;height:35px;border-radius:50%;background:#fff;display:flex;align-items:center;justify-content:center}
.social-foot i::after{content:"";width:13px;height:13px;border-radius:50%;background:var(--red)}
</style>
</head>
<body>
<header>
  <div class="topbar">
    <div class="contact-line">
      <span><svg width="14" height="12" viewBox="0 0 14 12"><path d="M7 0L0 6h2v6h4V8h2v4h4V6h2z" fill="#999"/></svg>Suite 210 Cedar Court 4,</span>
      <span><svg width="12" height="12" viewBox="0 0 12 12"><path d="M2 0l3 3-2 2c1 2 2 3 4 4l2-2 3 3-2 2C5 12 0 7 0 2z" fill="#999"/></svg>6014.5538270</span>
      <span><svg width="10" height="13" viewBox="0 0 10 13"><path d="M5 0a5 5 0 00-5 5c0 4 5 8 5 8s5-4 5-8a5 5 0 00-5-5zm0 7a2 2 0 110-4 2 2 0 010 4z" fill="#999"/></svg>hello@meadowfoxtrail.com</span>
    </div>
    <div class="social-top" aria-label="Social links"><i></i><i></i><i></i><i></i><i></i><i></i><i></i><i></i></div>
  </div>
  <div class="brand">
    <div class="brand-mark"></div>
    <div>
      <div class="brand-tag">WEB APPLICATION FOR CELLULAR NETWORK</div>
      <div class="brand-name">MeadowFoxTrail</div>
    </div>
  </div>
  <nav class="main-nav">
    <a class="nav-home" href="#"><svg viewBox="0 0 34 34"><path d="M17 3L2 17h5v13h8v-8h4v8h8V17h5z" fill="#fff"/></svg>HOME</a>
    <a class="nav-about" href="#"><svg viewBox="0 0 34 34"><circle cx="17" cy="10" r="7" fill="#fff"/><path d="M5 32c0-9 5-13 12-13s12 4 12 13z" fill="#fff"/></svg>ABOUT US</a>
    <a class="nav-products" href="#"><svg viewBox="0 0 34 34"><circle cx="17" cy="17" r="10" fill="none" stroke="#fff" stroke-width="7" stroke-dasharray="5 3"/><circle cx="17" cy="17" r="4" fill="#fff"/></svg>PRODUCTS &amp;<br>SERVICES</a>
    <a class="nav-news" href="#"><svg viewBox="0 0 34 34"><rect x="4" y="5" width="26" height="24" rx="2" fill="none" stroke="#fff" stroke-width="3"/><path d="M9 11h16M9 17h7M9 22h7M19 17h6v5h-6z" stroke="#fff" stroke-width="2.5" fill="none"/></svg>NEWS &amp;<br>UPDATES</a>
    <a class="nav-contact" href="#"><svg viewBox="0 0 34 34"><path d="M2 12c0-6 30-6 30 0v3h-7v-3H9v3H2z" fill="#fff"/><path d="M7 30l3-12h14l3 12z" fill="#fff"/><circle cx="17" cy="23" r="3" fill="var(--nav-contact)"/></svg>CONTACT US</a>
    <a class="nav-mail" href="#"><svg viewBox="0 0 34 34"><rect x="3" y="8" width="28" height="20" fill="#fff"/><path d="M3 8l14 11 14-11" stroke="var(--nav-mail)" stroke-width="3" fill="none"/></svg>WEBMAIL</a>
  </nav>
</header>

<section class="hero">
  <div class="slide-btn" style="left:93px;top:106px"><svg width="12" height="22"><path d="M11 1L1 11l10 10" stroke="#fff" fill="none" stroke-width="1.5"/></svg></div>
  <div class="hero-text">
    <h1>This Product also can be customized for specific</h1>
    <p>report that has been agreed between us and the customer before the system is integrated in the customer office.</p>
  </div>
  <div class="hero-visual" role="img" aria-label="Blue network globe illustration"></div>
  <div class="slide-btn" style="left:1002px;top:110px"><svg width="12" height="22"><path d="M1 1l10 10L1 21" stroke="#fff" fill="none" stroke-width="1.5"/></svg></div>
</section>

<section class="features">
  <article class="card" style="left:93px">
    <h2 style="position:absolute;left:12px;top:4px">OUR TEAM</h2>
    <div class="pager" style="left:248px;top:3px"><i><svg width="6" height="8"><path d="M5 0L1 4l4 4" stroke="#fff" fill="none"/></svg></i><i><svg width="6" height="8"><path d="M1 0l4 4-4 4" stroke="#fff" fill="none"/></svg></i></div>
    <div class="photo" role="img" aria-label="Photo of a smiling woman holding a cup" style="background:linear-gradient(90deg,#f6f6f6,#e8ddd2 60%,#f2e6da)"></div>
    <p>No other agency matches our pet industry experience, period. From serving on industry boards to managing media at trade shows, helping to grow associations, and</p>
    <div class="rule"></div>
  </article>
  <article class="card" style="left:417px">
    <h2 style="position:absolute;left:9px;top:0">OUR ORGANIZATION</h2>
    <div class="pager" style="left:245px;top:3px"><i><svg width="6" height="8"><path d="M5 0L1 4l4 4" stroke="#fff" fill="none"/></svg></i><i><svg width="6" height="8"><path d="M1 0l4 4-4 4" stroke="#fff" fill="none"/></svg></i></div>
    <div class="photo" role="img" aria-label="Close-up photo of fingers on a keyboard" style="background:linear-gradient(#3d8fbf,#c9dbe6 55%,#6f7f8c)"></div>
    <p>No other agency matches our pet industry experience, period. From serving on industry boards to managing media at trade shows, helping to grow associations, and</p>
    <div class="rule"></div>
  </article>
  <article class="card" style="left:741px">
    <h2 style="position:absolute;left:10px;top:2px">OUR VALUES</h2>
    <div class="pager" style="left:243px;top:3px"><i><svg width="6" height="8"><path d="M5 0L1 4l4 4" stroke="#fff" fill="none"/></svg></i><i><svg width="6" height="8"><path d="M1 0l4 4-4 4" stroke="#fff" fill="none"/></svg></i></div>
    <div class="photo" role="img" aria-label="Photo of an internet speed test gauge" style="left:9px;background:radial-gradient(circle at 60% 45%,#2f5a6a,#17232b 70%)"></div>
    <p>No other agency matches our pet industry experience, period. From serving on industry boards to managing media at trade shows, helping to grow associations, and</p>
    <div class="rule"></div>
  </article>
</section>

<section class="product-samples">
  <h2 style="position:absolute;left:105px;top:14px">SAMPLE OF OUR PRODUCT</h2>
  <div class="pager" style="left:984px;top:18px"><i><svg width="6" height="8"><path d="M5 0L1 4l4 4" stroke="#fff" fill="none"/></svg></i><i><svg width="6" height="8"><path d="M1 0l4 4-4 4" stroke="#fff" fill="none"/></svg></i></div>
  <div class="photo" role="img" aria-label="Dark photo of a computer keyboard" style="left:105px;background:radial-gradient(circle at 45% 30%,#3a3a3a,#161616 75%)">
    <div class="zoom"><svg width="32" height="32" viewBox="0 0 32 32"><circle cx="13" cy="13" r="10" fill="none" stroke="#fff" stroke-width="4"/><path d="M20 20l9 9M13 8v10M8 13h10" stroke="#fff" stroke-width="4"/></svg></div>
  </div>
  <div class="photo" role="img" aria-label="Photo of a businessman working on a laptop" style="left:428px;background:linear-gradient(90deg,#8f96a0,#c9c2b3 50%,#e3ddd2)"></div>
  <div class="photo" role="img" aria-label="Photo of students working in a café" style="left:751px;background:linear-gradient(90deg,#6b5546,#c9b49d 50%,#9a8676)"></div>
</section>

<footer class="footer">
  <nav><span>Home</span><span>About Us</span><span>&nbsp;Products &amp; Services</span><span>News &amp; Updates</span><span>Contact Us</span><span>Webmail</span></nav>
  <small>© 2014 Company Name.&nbsp; All right reserved.&nbsp; Term of Use</small>
  <div class="social-foot" aria-label="Social links"><i></i><i></i><i></i><i></i></div>
</footer>
</body>
</html>
```